New Crowdfunding site Fundlark needs banner ads

I’m looking for 4 standard size banner ads for www.fundlark.example to be used by LinkaDeal Affiliates in order to bring new crowdfunding projects to the platform.
728x90
160x600
300x250
180x160

Succesful designers will put on our Mentors list so that the project owner can also get their specific project banners from our designers. Designers can also become our affiliates either to promote Fundlark.example or individual projects.
Updates

Please note updated brief

Thank you to those that have submitted designs so far.
Please be reminded that the invitation will close tomorrow after which we will make our choice

Thanks for input so far.
Please note project closes tomorrow (Sunday) after which we will choose.

Target Market(s)

Target is a project owner with a project requiring $10,000 or more in any field including business and/or non-profits. Any country.
Inventors, creatives, communities, hardware or software, consumer items,

Industry/Entity Type

Crowdfunding

Font styles to use
Sans Serif

Requirements
Must have
• Clear button call to action based on our USPs shown on the home page but especially the use of Affiliate Networks to promote their project to the widest possible audience.

Text and button text should be editable (see png preference).
Call to action could be based on "Free Crowdfunding Consultation - is your project viable" or "Get Your Free Guide to Succesful Crowdfunding"
Nice to have
• .png format preferred with separate objects.
Some animation preferred in the button.

```html
<!DOCTYPE html>
<html lang="en">
<head>
<meta charset="utf-8">
<title>Fundlark – Free Crowdfunding Consultation banner</title>
<link rel="stylesheet" href="https://fonts.googleapis.com/css2?family=Montserrat:wght@400;500;600&family=PT+Sans:wght@400&display=swap">
<style>
  :root {
    --stage: #151515;
    --navy: #0c4a7a;
    --sky-text: #93d6f5;
    --white: #ffffff;
    --green: #1fba1f;
    --green-border: #d6f2d6;
    --brand-blue: #1a4a7c;
  }
  html, body {
    margin: 0;
    width: 1200px;
    height: 900px;
    overflow: hidden;
    background: var(--stage);
  }
  .banner {
    position: absolute;
    left: 375px;
    top: 262px;
    width: 450px;
    height: 375px;
    overflow: hidden;
    background: var(--navy);
    font-family: "Montserrat", sans-serif;
  }
  .banner__backdrop {
    position: absolute;
    inset: 0;
    width: 100%;
    height: 100%;
  }
  .headline {
    position: absolute;
    left: 21px;
    top: 14px;
    margin: 0;
    color: var(--white);
    font-weight: 400;
    font-size: 39px;
    line-height: 50px;
    letter-spacing: 0.2px;
  }
  .subhead {
    position: absolute;
    left: 21px;
    top: 122px;
    margin: 0;
    color: var(--sky-text);
    font-weight: 400;
    font-size: 30px;
    line-height: 36px;
  }
  .cta {
    position: absolute;
    left: 249px;
    top: 184px;
    width: 179px;
    height: 60px;
    box-sizing: border-box;
    border: 2px solid var(--green-border);
    border-radius: 8px;
    background: var(--green);
    color: var(--white);
    font-family: "Montserrat", sans-serif;
    font-weight: 600;
    font-size: 23px;
    display: flex;
    align-items: center;
    justify-content: center;
    text-decoration: none;
  }
  .brand__dot {
    position: absolute;
    left: 30px;
    top: 255px;
    width: 96px;
    height: 96px;
    border-radius: 50%;
    background: var(--brand-blue);
  }
  .brand__name {
    position: absolute;
    left: 157px;
    top: 296px;
    margin: 0;
    color: var(--brand-blue);
    font-weight: 500;
    font-size: 35px;
    line-height: 40px;
    letter-spacing: 0.5px;
  }
  .brand__tagline {
    position: absolute;
    left: 158px;
    top: 337px;
    margin: 0;
    color: var(--brand-blue);
    font-family: "PT Sans", sans-serif;
    font-size: 20px;
    line-height: 24px;
  }
</style>
</head>
<body>
  <div class="banner">
    <svg class="banner__backdrop" viewBox="0 0 300 250" preserveAspectRatio="none" aria-hidden="true">
      <path d="M0,146 Q110,186 300,181 L300,194 Q130,198 0,150 Z" fill="var(--green)"/>
      <path d="M0,150 Q130,198 300,194 L300,250 L0,250 Z" fill="var(--white)"/>
    </svg>

    <h1 class="headline">Free Crowdfunding<br>Consultation</h1>
    <p class="subhead">Is your project viable?</p>
    <a class="cta" href="#">Learn more</a>

    <span class="brand__dot" aria-hidden="true"></span>
    <p class="brand__name">FUNDLARK</p>
    <p class="brand__tagline">Project + Crowd = Funding</p>
  </div>
</body>
</html>
```